Hollowmere Farm Promotional Leaflet

The team at Hollowmere Farm can help with every aspect of managing and enhancing your home from housekeeping and professional cleaning, laundry and ironing to providing chic and contemporary flower arrangements and even food for your pets!We take pride in providing high-end, consistent and reliable professional services bespoke to you. Whether you are a busy professional working long hours, a stay-at home parent or retired; having professional help in the home gives you time to spend on the things you enjoy.We are providing a very upmarket, highly professional service and need an A5 promotional leaflet to be designed. Please refer to www.hollowmerefarm-example.co.uk and see the section on 'Home Management'The leaflet should incorporate the Hollowmere Farm logo without the 'tipi', and any suitable photography images used on the home page of the website or the 'home management' section.

Target Market(s)

high-end, affluent owners of luxury homes

Industry/Entity Type

Farm

Contact Information for Business Card

The business card design needs to be suitable for use across all of Hollowmere Farm businesses, specifically:
Hollowmere Farm Home Management - otherwise known as Hollowmere Farm @ Home (this uses the typographical logo
Hollowmere Farm Weddings & Events - this uses the 'tipi' logo

Requirements
Must have
• Design in keeping with the look and feel of the logo and website design
• www.hollowmerefarm-example.co.uk

```html
<!DOCTYPE html>
<html lang="en">
<head>
<meta charset="utf-8">
<title>Hollowmere Farm – Business Card</title>
<link rel="stylesheet" href="https://fonts.googleapis.com/css2?family=Open+Sans:wght@400;600&display=swap">
<style>
  :root {
    --page-bg: #e9e7e8;
    --card-white: #fbfafb;
    --brand-pink: #d81b5f;
    --brand-gold: #d4a94c;
    --pattern-pink: #f6dfe8;
    --text-grey: #555055;
    --text-white: #ffffff;
  }
  * { box-sizing: border-box; margin: 0; padding: 0; }
  html, body {
    width: 1200px; height: 900px; overflow: hidden;
    background: var(--page-bg);
    font-family: "Open Sans", Arial, sans-serif;
  }
  .canvas {
    width: 1200px; height: 900px;
    display: flex; flex-direction: column; align-items: center; justify-content: center;
    gap: 40px;
  }
  .card {
    position: relative; width: 700px; height: 400px;
    background: var(--card-white);
    box-shadow: 0 6px 18px rgba(0,0,0,0.18);
    overflow: hidden;
  }
  /* Card back */
  .card-back__pattern {
    position: absolute; inset: 0;
    background: linear-gradient(135deg, var(--card-white) 0%, var(--pattern-pink) 50%, var(--card-white) 100%);
    opacity: 0.7;
  }
  .card-back__content {
    position: absolute; inset: 0;
    display: flex; flex-direction: column; align-items: center; justify-content: center;
    gap: 22px;
  }
  .brand-name {
    font-weight: 600; color: var(--brand-pink);
    font-size: 54px; letter-spacing: 0.5px; line-height: 1;
    white-space: nowrap;
  }
  .card-back__url {
    font-size: 15px; letter-spacing: 4px; color: var(--text-grey);
  }
  /* Card front */
  .card-front__wave { position: absolute; inset: 0; }
  .card-front__brand {
    position: absolute; left: 46px; top: 152px;
  }
  .card-front__brand .brand-name { font-size: 36px; }
  .contact {
    position: absolute; right: 24px; top: 62px;
    text-align: right; color: var(--text-white);
    font-size: 12px; line-height: 1.5;
    white-space: nowrap;
  }
  .contact__name { font-weight: 600; font-size: 15px; }
  .contact__role { margin-bottom: 10px; font-size: 14px; }
  .contact__line { display: flex; justify-content: flex-end; align-items: center; gap: 7px; }
  .contact__icon { width: 12px; height: 12px; flex: none; }
</style>
</head>
<body>
<main class="canvas">

  <section class="card card-back">
    <div class="card-back__pattern" role="img" aria-label="Faint repeating brand-name pattern in pale pink"></div>
    <div class="card-back__content">
      <p class="brand-name">Hollowmere Farm</p>
      <p class="card-back__url">www.hollowmerefarm-example.co.uk</p>
    </div>
  </section>

  <section class="card card-front">
    <svg class="card-front__wave" viewBox="0 0 700 400" width="700" height="400" aria-hidden="true">
      <path d="M548,0 C420,60 402,170 370,245 C330,330 230,370 0,372 L0,384 C240,382 345,340 384,250 C414,175 430,62 562,0 Z" fill="var(--brand-gold)"/>
      <path d="M590,0 L700,0 L700,400 L110,400 C260,385 360,330 395,250 C425,180 440,60 590,0 Z" fill="var(--brand-pink)"/>
    </svg>

    <div class="card-front__brand">
      <p class="brand-name">Hollowmere Farm</p>
    </div>

    <div class="contact">
      <p class="contact__name">DANIEL HART</p>
      <p class="contact__role">CEO/FOUNDER</p>
      <p>Hollowmere Farm</p>
      <p>Mill Lane, Ashby Combe</p>
      <p>Somerset TA99 1ZZ, GB</p>
      <p class="contact__line">+44 7700 900482
        <svg class="contact__icon" viewBox="0 0 16 16" aria-hidden="true"><path d="M3 1h3l1.5 4-2 1.2a9 9 0 0 0 4.3 4.3L11 8.5l4 1.5v3a2 2 0 0 1-2 2A13 13 0 0 1 1 3a2 2 0 0 1 2-2z" fill="var(--text-white)"/></svg>
      </p>
      <p class="contact__line">www.hollowmerefarm-example.co.uk
        <svg class="contact__icon" viewBox="0 0 16 16" aria-hidden="true"><circle cx="8" cy="8" r="6.5" fill="none" stroke="var(--text-white)" stroke-width="1.5"/><path d="M1.5 8h13M8 1.5c-3 3.5-3 9.5 0 13M8 1.5c3 3.5 3 9.5 0 13" fill="none" stroke="var(--text-white)" stroke-width="1.2"/></svg>
      </p>
    </div>
  </section>

</main>
</body>
</html>
```